Coach/consultant in conflict and challenge needs an enticing flyer

I need a double sided DL flyer design that will describe my work in helping people meet conflict and emotional challenge so they can learn and grow from these difficulties. I want to give a flavour of my style through fresh colours, repeated images used differently (the spiral), and a sense of positivity around conflict and difficulty. I want to attract people who are keen to do things differently and want to engage with creative processes rather than getting stuck in familiar patterns. My work is creative and often includes use of story, images and fables, so I want to convey that as well. I also place the work in a spiritual context, but grounded in practicality so I don't want it to seem New Age or flakey. I want something that seems innovative, professional and intriguing. I've included a sample of something I mocked up in word and also a copy of a flyer for Marla Quennet's Ember Gathering that inspired me to get a DL flyer. I want the design to communicate trust and transformation and engaging with fresh ways of doing things by moving past old habits

Target Market(s)

Mid 30s plus women and men who want to change their approach to conflict and emotional difficulties and are willing to take the creative and challenging journey to do that

Industry/Entity Type

Learn

Colors
acd136
00a990

Requirements
Must have
• a shift in the use of the spiral image,
• use of image of me (Norah)
• bright fresh colours olours that represent growth and transformation--I've suggested lime green as it suggests a sense of growth
• easy to read text
Nice to have
• Interesting non-traditional fonts perhaps text in a contemporary sans serif and another brush script font (like the Ember Gathering example)
• bleed to the edge and run off the page images or text
Should not have
• anything that represents too much tradition or stuckness

```html
<!DOCTYPE html>
<html lang="en">
<head>
<meta charset="utf-8">
<title>Norah Vellacott – DL Flyer</title>
<link href="https://fonts.googleapis.com/css2?family=Lato:wght@400;700&family=Ubuntu:wght@400;500;700&family=Roboto+Condensed:wght@700&display=swap" rel="stylesheet">
<style>
  :root {
    --lime: #acd136;
    --teal: #00a990;
    --paper: #f3f4f2;
    --paper-deep: #e9ebe7;
    --ink: #2a2a2a;
    --brown: #6b3f27;
    --spiral-soft: #c9ab8c;
    --spiral-fade: #ece3d9;
    --white: #ffffff;
  }
  * { box-sizing: border-box; margin: 0; padding: 0; }
  html, body { width: 1200px; height: 1200px; overflow: hidden; background: var(--white); }
  body { position: relative; font-family: "Lato", sans-serif; color: var(--ink); }

  .flyer-side {
    position: absolute;
    width: 926px;
    height: 450px;
    overflow: hidden;
    background: linear-gradient(135deg, var(--paper) 0%, var(--white) 45%, var(--paper-deep) 100%);
  }
  .flyer-front { left: 126px; top: 86px; }
  .flyer-back { left: 128px; top: 638px; }

  .brush-band { position: absolute; inset: 0; width: 100%; height: 100%; }

  .abs { position: absolute; }

  .title {
    left: 26px; top: 18px;
    font-family: "Lato", sans-serif; font-weight: 700;
    font-size: 50px; color: var(--white); letter-spacing: 0.5px;
  }

  .value-tag {
    font-family: "Ubuntu", sans-serif;
    font-weight: 500;
    padding: 2px 14px 4px;
    background: var(--lime);
    clip-path: polygon(4% 18%, 20% 6%, 50% 12%, 80% 2%, 100% 14%, 96% 50%, 100% 86%, 70% 96%, 40% 88%, 12% 98%, 0% 80%, 5% 50%);
    white-space: nowrap;
  }
  .front-tag { top: 168px; font-size: 26px; font-weight: 700; color: var(--ink); }

  .body-copy { font-size: 14.5px; line-height: 18.5px; color: var(--ink); }
  .front-copy { left: 28px; width: 560px; }

  .call-line {
    left: 28px; top: 336px;
    font-family: "Roboto Condensed", sans-serif; font-weight: 700;
    font-size: 37px; color: var(--ink);
  }
  .call-line .call-label { color: var(--brown); margin-right: 20px; }

  .web-line { left: 32px; top: 392px; font-size: 13px; letter-spacing: 7.4px; color: var(--ink); }

  .spiral-art {
    left: 598px; top: 32px; width: 306px; height: 288px;
    border-radius: 50%;
    background: radial-gradient(ellipse at 50% 50%, var(--spiral-soft) 0%, var(--spiral-fade) 60%, transparent 72%);
  }

  .back-copy { left: 22px; width: 542px; text-align: justify; hyphens: auto; }
  .back-tag { top: 248px; font-size: 21px; color: var(--ink); font-weight: 400; }

  .contact { font-size: 14.5px; line-height: 24px; color: var(--ink); }
  .contact-row { display: flex; align-items: center; gap: 6px; }
  .contact-row .icon { width: 14px; height: 14px; flex: none; }
  .contact-row .indent { padding-left: 20px; }

  .portrait {
    left: 646px; top: 0; width: 280px; height: 450px;
    background: linear-gradient(180deg, #d8d3cc 0%, #c4bab0 32%, #e26a2c 58%, #d2521b 100%);
  }

  .sign-name {
    right: 300px; top: 382px;
    font-family: "Ubuntu", sans-serif; font-weight: 500;
    font-size: 21px; color: var(--lime); text-align: right;
  }
  .sign-cred {
    right: 300px; top: 413px;
    font-size: 14.5px; color: var(--white); text-align: right;
  }
</style>
</head>
<body>

<section class="flyer-side flyer-front">
  <svg class="brush-band" viewBox="0 0 926 450" preserveAspectRatio="none" aria-hidden="true">
    <polygon fill="var(--teal)" points="0,0 464,0 448,14 440,30 420,42 410,60 380,72 350,80 300,90 250,98 200,106 170,110 140,104 100,112 70,106 40,110 20,104 0,108"/>
    <polygon fill="var(--lime)" points="265,450 276,436 320,430 370,424 420,410 470,404 520,398 560,386 600,384 640,376 680,374 700,362 740,366 760,352 790,360 800,372 830,374 850,372 870,378 900,370 926,366 926,450"/>
  </svg>

  <h1 class="abs title">Norah Vellacott</h1>

  <span class="abs value-tag front-tag" style="left:22px">courage</span>
  <span class="abs value-tag front-tag" style="left:164px">listening</span>
  <span class="abs value-tag front-tag" style="left:318px">creativity</span>

  <p class="abs body-copy front-copy" style="top:220px">Challenge, change and conflict are a natural part of life. When we greet them with courage, and listen to what they tell us, we grow in wisdom, resilience and creativity.</p>
  <p class="abs body-copy front-copy" style="top:278px">Norah Vellacott is a coach, educator and mediator. She works with people who want to harvest the fruits of challenge and conflict so they live life differently.</p>

  <p class="abs call-line"><span class="call-label">CALL NOW</span>0400 555 123</p>
  <p class="abs web-line">www.norahvellacott.com</p>

  <div class="abs spiral-art" role="img" aria-label="Brown brush-stroke spiral artwork"></div>
</section>

<section class="flyer-side flyer-back">
  <svg class="brush-band" viewBox="0 0 926 450" preserveAspectRatio="none" aria-hidden="true">
    <polygon fill="var(--lime)" points="0,0 536,0 520,10 500,16 460,20 420,28 380,34 330,44 300,40 260,52 220,48 180,56 140,52 100,58 60,52 30,58 0,52"/>
    <polygon fill="var(--teal)" points="240,450 262,440 300,432 340,426 370,418 400,404 440,400 480,394 520,378 560,374 600,368 640,364 700,370 760,360 820,356 880,350 926,348 926,450"/>
  </svg>

  <p class="abs body-copy back-copy" style="top:84px">Consult with Norah to address challenges in your life, relationship, group or organisation. Through listening, conversation and creative processes, you will discover what your challenge is asking of you. Norah Vellacott is a skilled facilitator who works to shift people’s responses from reactivity to creativity.</p>
  <p class="abs body-copy back-copy" style="top:174px">With many years’ experience in coaching and mentorship, mediation and narrative processes, Norah supports you to uncover unique responses to difficult situations.</p>

  <span class="abs value-tag back-tag" style="left:16px">consultations</span>
  <span class="abs value-tag back-tag" style="left:188px">workshops</span>
  <span class="abs value-tag back-tag" style="left:352px">speaking</span>
  <span class="abs value-tag back-tag" style="left:484px">articles</span>

  <div class="abs contact" style="left:24px; top:310px">
    <div class="contact-row">
      <svg class="icon" viewBox="0 0 16 16" aria-hidden="true"><path fill="var(--teal)" d="M3 1l3 3-1.5 2a9 9 0 0 0 5.5 5.5L12 10l3 3-2 2C7 15 1 9 1 3z"/></svg>
      <span>0400 555 123</span>
    </div>
    <div class="contact-row"><span class="indent">+61 3 5550 1234</span></div>
    <div class="contact-row">
      <svg class="icon" viewBox="0 0 16 16" aria-hidden="true"><rect x="1" y="4" width="14" height="10" fill="var(--teal)"/><path d="M1 4l7 6 7-6" fill="none" stroke="var(--white)" stroke-width="1.4"/></svg>
      <span>norah@norahvellacott.com</span>
    </div>
  </div>

  <div class="abs contact" style="left:268px; top:324px">
    <div class="contact-row">
      <svg class="icon" viewBox="0 0 16 16" aria-hidden="true"><circle cx="8" cy="8" r="6.5" fill="none" stroke="var(--teal)" stroke-width="1.6"/><path d="M1.5 8h13M8 1.5c-3 3-3 10 0 13M8 1.5c3 3 3 10 0 13" fill="none" stroke="var(--teal)" stroke-width="1.2"/></svg>
      <span>norahvellacott.com</span>
    </div>
    <div class="contact-row"><span class="indent">ABN 12 345 678 90</span></div>
  </div>

  <div class="abs portrait" role="img" aria-label="Portrait photograph of Norah in an orange knitted top"></div>

  <p class="abs sign-name">Norah Vellacott</p>
  <p class="abs sign-cred">PhD, MCR, BAppSci, DipHum, AssDipEd</p>
</section>

</body>
</html>
```